Brivomark Business Card

Brivomark is a young and energetic software development consultancy. We spend our time on the road working with clients on their sites an meeting new potential customers and employees!

We need a sharp, vibrant and memorable business card that will inspires those that receive it to look after it as it oozes quality and is a nice thing in its own right.

We like bold colours and distinctive design. So show us what you can do.

In terms of information on the card, it would be good to see:

* Our logo (Obviously :) )
* Employee name
* Email
* Website address
* Mobile number
* Full company name (Brivomark ltd)
* Registered company number
* Registered company address

Industry/Entity Type

Software

Requirements
Nice to have
• We are thinking that having a QR Code on the business card could be a good way of adding active marketing. It would be good to see if you are able to merge the kind of element in to your designs!

Maybe something special could be achieved using a visual QR Code like those produced at http://www.quenprint-example.com/ ? You have our media so feel free to have a play.

```html
<!DOCTYPE html>
<html lang="en">
<head>
<meta charset="utf-8">
<title>Brivomark ltd — Business Card</title>
<link href="https://fonts.googleapis.com/css2?family=Raleway:wght@300;400&display=swap" rel="stylesheet">
<style>
  :root {
    --stage: #1c1c1c;
    --card-black: #0b0b0b;
    --card-white: #ececec;
    --brand-red: #d21f3c;
    --rule-dark: #111111;
    --text-grey: #9a9a9a;
    --text-dark: #222222;
    --text-light: #e6e6e6;
  }
  * { margin: 0; padding: 0; box-sizing: border-box; }
  html, body {
    width: 1200px; height: 720px; overflow: hidden;
    background: var(--stage);
    font-family: "Raleway", sans-serif;
  }
  .stage {
    position: relative; width: 1200px; height: 720px;
    display: flex; align-items: center; justify-content: center; gap: 60px;
  }
  .card {
    position: relative; width: 500px; height: 286px;
    box-shadow: 0 10px 30px rgba(0,0,0,.5);
  }

  /* Front */
  .card-front {
    background: linear-gradient(135deg, #2a2a2a 0%, var(--card-black) 45%, var(--card-black) 100%);
    border-bottom: 8px solid var(--brand-red);
    border-left: 8px solid var(--brand-red);
    display: flex; align-items: center; justify-content: center; gap: 16px;
  }
  .front-mark {
    width: 28px; height: 28px; background: var(--brand-red);
  }
  .front-name {
    font-weight: 300; font-size: 62px; letter-spacing: 2px;
    color: var(--text-light); text-transform: uppercase;
  }

  /* Back */
  .card-back {
    background: var(--brand-red);
    padding: 7px;
  }
  .back-inner {
    width: 100%; height: 100%;
    border: 3px solid var(--rule-dark);
    background: var(--brand-red);
    padding: 4px;
  }
  .back-face {
    position: relative; width: 100%; height: 100%;
    background: radial-gradient(circle at 55% 40%, #f6f6f6 0%, var(--card-white) 60%, #d9d9d9 100%);
  }
  .company-block { position: absolute; left: 22px; top: 24px; }
  .company-name {
    display: flex; align-items: center; gap: 8px;
    font-weight: 300; font-size: 36px; color: var(--text-grey);
    text-transform: uppercase; letter-spacing: 1px;
  }
  .company-name .dot { width: 14px; height: 14px; background: var(--brand-red); }
  .company-number {
    margin-top: 4px; font-size: 9px; letter-spacing: 3.2px;
    color: #666; text-transform: uppercase;
  }
  .contact-list {
    position: absolute; right: 24px; bottom: 22px;
    list-style: none; font-size: 14px; color: var(--text-dark);
    font-weight: 400; line-height: 1.45;
  }
  .contact-list li { display: flex; align-items: flex-start; gap: 8px; }
  .contact-list svg { width: 12px; height: 12px; margin-top: 4px; flex: none; fill: var(--brand-red); }
</style>
</head>
<body>
<main class="stage">
  <section class="card card-front" aria-label="Card front">
    <span class="front-mark"></span>
    <span class="front-name">Brivomark</span>
  </section>

  <section class="card card-back" aria-label="Card back">
    <div class="back-inner">
      <div class="back-face">
        <div class="company-block">
          <div class="company-name"><span class="dot"></span>Brivomark ltd</div>
          <div class="company-number">Registered company number</div>
        </div>
        <ul class="contact-list">
          <li>
            <svg viewBox="0 0 12 12" aria-hidden="true"><path d="M3 1l2 2.5-1.2 1.2a6 6 0 0 0 3.5 3.5L8.5 7 11 9l-1.3 1.8C5.5 11 1 6.5 1.2 2.3z"/></svg>
            <span>0800-555-019</span>
          </li>
          <li>
            <svg viewBox="0 0 12 12" aria-hidden="true"><path d="M1 2h10v8H1zM1.8 2.8L6 6.5l4.2-3.7" stroke="#fff" stroke-width=".8"/></svg>
            <span>e-mail@brivomark-example.com</span>
          </li>
          <li>
            <svg viewBox="0 0 12 12" aria-hidden="true"><circle cx="6" cy="6" r="5"/><path d="M1 6h10M6 1c-2 3-2 7 0 10M6 1c2 3 2 7 0 10" stroke="#fff" stroke-width=".6" fill="none"/></svg>
            <span>www.brivomark-example.com</span>
          </li>
          <li>
            <svg viewBox="0 0 12 12" aria-hidden="true"><path d="M6 11.5S2 7 2 4.5a4 4 0 0 1 8 0C10 7 6 11.5 6 11.5z"/><circle cx="6" cy="4.5" r="1.4" fill="#fff"/></svg>
            <span>your address will<br>be here</span>
          </li>
        </ul>
      </div>
    </div>
  </section>
</main>
</body>
</html>
```